Harbor Shell Interiors web design

We need to relaunch my commercial and retail interior design + construction company after being out of the industry's for 10 plus years.

```html
<!DOCTYPE html>
<html lang="en">
<head>
<meta charset="utf-8">
<title>Harbor Shell Interiors</title>
<link href="https://fonts.googleapis.com/css2?family=Krona+One&family=Lato:wght@300;400;700;900&display=swap" rel="stylesheet">
<style>
:root{
  --blue:#0a8df0;
  --ink:#111111;
  --text:#4a4a4a;
  --grey-bg:#f4f4f4;
  --white:#ffffff;
  --black:#0b0b0b;
  --line:#d9d9d9;
}
*{margin:0;padding:0;box-sizing:border-box}
html,body{width:1200px;height:4732px;overflow:hidden}
body{position:relative;background:var(--white);font-family:'Lato',sans-serif;color:var(--text)}
.abs{position:absolute}
.heading{font-family:'Krona One',sans-serif;color:var(--ink);font-weight:400}
.btn{position:absolute;background:var(--blue);color:var(--white);font-size:12px;font-weight:700;letter-spacing:.5px;display:flex;align-items:center;justify-content:center;text-transform:uppercase}
.photo{position:absolute}
.brand{position:absolute;display:flex;align-items:center;gap:12px}
.brand-mark{width:22px;height:22px;background:var(--blue)}
.brand-name{font-family:'Krona One',sans-serif;font-size:17px;line-height:20px;color:var(--ink);width:190px}

/* header */
.topbar{left:672px;top:0;width:528px;height:34px;background:var(--black);clip-path:polygon(24px 0,100% 0,100% 100%,0 100%);color:var(--white);font-size:14px;display:flex;align-items:center;gap:26px;padding-left:50px}
.topbar span{display:flex;align-items:center;gap:7px}
.nav{left:560px;top:56px;display:flex;gap:48px;font-size:12px;color:var(--ink);font-weight:700}
/* hero */
.hero{left:0;top:102px;width:1200px;height:530px;background:linear-gradient(180deg,#6f6a62 0%,#54524e 50%,#4a4a3c 100%)}
.hero-title{left:0;top:240px;width:1200px;text-align:center;font-size:44px;line-height:56px;color:var(--white)}
.hero-sub{left:0;top:376px;width:1200px;text-align:center;font-size:32px;font-weight:300;color:var(--white)}
/* about */
.about-title{left:141px;top:735px;font-size:34px}
.about-copy{left:141px;top:796px;width:430px;font-size:12px;line-height:23px}
.about-copy p+p{margin-top:8px}
.work-in{left:141px;top:1004px;font-family:'Krona One',sans-serif;font-size:17px;color:var(--ink)}
.work-in b{color:var(--blue);font-weight:400}
.frame-line{position:absolute;background:var(--blue)}
/* services */
.services{left:0;top:1176px;width:1200px;height:662px;background:var(--grey-bg)}
.center-title{left:0;width:1200px;text-align:center;font-size:36px}
.services-desc{left:260px;top:1314px;width:680px;text-align:center;font-size:12px;line-height:23px}
.service-label{position:absolute;width:212px;text-align:center;font-family:'Krona One',sans-serif;font-size:17px;line-height:27px;color:var(--ink)}
/* expertise */
.exp-box{left:141px;top:2016px;width:447px;height:296px;background:var(--white)}
.exp-title{left:178px;top:2090px;font-size:36px;line-height:47px}
.exp-frame{left:157px;top:2326px;width:447px;height:296px;border:1.5px solid var(--blue)}
.exp-copy{left:630px;top:2344px;width:405px;font-size:12px;line-height:23px}
.exp-copy p+p{margin-top:10px}
/* portfolio */
.portfolio-note{color:#e9e9e9;font-size:12px;line-height:23px;text-align:center;display:flex;align-items:center;justify-content:center;padding:0 44px}
/* testimonials */
.testimonials{left:0;top:3398px;width:1200px;height:572px;background:var(--grey-bg)}
.t-card{position:absolute;width:393px;height:183px;background:var(--white);box-shadow:0 6px 24px rgba(0,0,0,.07);padding:66px 40px 0 40px;font-size:12px;line-height:21px}
.t-card:after{content:"";position:absolute;left:0;bottom:-26px;border-top:26px solid var(--white);border-right:26px solid transparent}
.t-quote{position:absolute;left:40px;top:22px}
.avatar{position:absolute;width:66px;height:66px;border-radius:50%;background:linear-gradient(160deg,#9aa3ad,#4f5863);border:4px solid var(--white);box-shadow:0 2px 8px rgba(0,0,0,.15)}
.t-name{position:absolute;font-family:'Krona One',sans-serif;font-size:13px;color:var(--ink)}
.t-role{position:absolute;font-size:12px}
.arrow{position:absolute;width:63px;height:63px;border-radius:50%;border:1.5px dashed #333;display:flex;align-items:center;justify-content:center;background:var(--white)}
.arrow.next{border-color:var(--blue)}
/* contact */
.field{position:absolute;height:40px;border:1px solid var(--line);display:flex;align-items:center;font-size:12px;color:var(--text)}
.field .ico{width:40px;height:100%;border-right:1px solid var(--line);display:flex;align-items:center;justify-content:center;flex-shrink:0}
.field .lbl{padding-left:12px}
.field .lbl i{color:#e02020;font-style:normal}
.field.msg{align-items:flex-start}
.field.msg .lbl{padding-top:10px}
.field.msg .ico{align-items:flex-start;padding-top:10px}
/* footer */
.footer{left:0;top:4478px;width:1200px;height:209px;background:var(--black)}
.footer .brand-name{color:var(--white)}
.footer-nav{left:497px;top:4548px;display:flex;gap:62px;font-size:12px;color:var(--white)}
.f-info{position:absolute;display:flex;align-items:center;gap:10px;color:var(--white);font-size:12px;line-height:18px}
.f-info .circ{width:28px;height:28px;border-radius:50%;border:1.5px solid var(--blue);display:flex;align-items:center;justify-content:center;flex-shrink:0}
.f-info b{font-weight:700}
.legal{left:0;top:4687px;width:1200px;height:45px;background:var(--blue)}
.legal-text{left:141px;top:4702px;font-size:12px;color:var(--white)}
.social{position:absolute;top:4696px;width:28px;height:28px;border-radius:50%;border:1.5px solid var(--white)}
</style>
</head>
<body>

<!-- header -->
<div class="brand" style="left:141px;top:22px"><div class="brand-mark"></div><div class="brand-name">Harbor Shell Interiors</div></div>
<div class="abs topbar">
  <span><svg width="14" height="14" viewBox="0 0 24 24"><path fill="#0a8df0" d="M6.6 10.8a15 15 0 0 0 6.6 6.6l2.2-2.2c.3-.3.7-.4 1-.2 1.1.4 2.3.6 3.6.6.6 0 1 .4 1 1V20c0 .6-.4 1-1 1A17 17 0 0 1 3 4c0-.6.4-1 1-1h3.5c.6 0 1 .4 1 1 0 1.3.2 2.5.6 3.6.1.3 0 .7-.2 1z"/></svg>03 5550 1482</span>
  <span><svg width="14" height="12" viewBox="0 0 24 18"><rect width="24" height="18" rx="2" fill="#0a8df0"/><path d="M1 2l11 8 11-8" stroke="#0b0b0b" stroke-width="2" fill="none"/></svg>info@harborshell.com</span>
</div>
<nav class="abs nav"><span>HOME</span><span>SERVICES</span><span>PORTFOLIO</span><span>CONTACT</span></nav>
<div class="btn" style="left:945px;top:48px;width:114px;height:34px;font-weight:400">GET A QUOTE</div>

<!-- hero -->
<div class="photo hero" role="img" aria-label="Modern open-plan office interior with desks, chairs and yellow accent walls"></div>
<div class="abs" style="left:0;top:102px;width:1200px;height:530px;background:rgba(0,0,0,.25)"></div>
<h1 class="abs heading hero-title">Commercial and Retail Interior<br>Design, Fitment &amp; Construction</h1>
<div class="abs hero-sub">10+ Years of Experience</div>
<div class="btn" style="left:512px;top:443px;width:176px;height:35px;font-weight:400">VIEW OUR PORTFOLIO</div>

<!-- about -->
<h2 class="abs heading about-title">About Us</h2>
<div class="abs about-copy">
  <p>At Harbor Shell Interiors, We Were Founded With Your Needs At The Forefront—a Dedication To Delivering A Transformative Leap In Results For Your Commercial And Retail Projects. Our Pride Lies In Surpassing Client Expectations, Achieved Through Meticulous Planning And Proactive Problem-solving Before Challenges Ever Surface."</p>
  <p>Guided By The Expertise Of Interior Designer And Commercial Builder, Mr. Daniel Ferrow Since 1994, Our Dedicated Team Seamlessly Manages Every Facet Of Your Project.</p>
</div>
<div class="abs work-in">We Work In <b>Australia.</b></div>
<div class="btn" style="left:141px;top:1044px;width:116px;height:34px;font-weight:400">CONTACT US</div>
<div class="frame-line" style="left:1084px;top:837px;width:6px;height:253px"></div>
<div class="frame-line" style="left:897px;top:1084px;width:193px;height:6px"></div>
<div class="photo" style="left:615px;top:713px;width:143px;height:167px;background:linear-gradient(150deg,#d8cf9a,#6d6a5c)" role="img" aria-label="Office interior with yellow feature wall"></div>
<div class="photo" style="left:772px;top:713px;width:287px;height:250px;background:linear-gradient(160deg,#b9c6d3,#8a7e64 60%,#d8862e)" role="img" aria-label="Builders in hard hats reviewing plans at a construction site"></div>
<div class="photo" style="left:615px;top:893px;width:143px;height:169px;background:linear-gradient(160deg,#cfd2d0,#6e6a55)" role="img" aria-label="Construction workers on site"></div>
<div class="photo" style="left:772px;top:975px;width:128px;height:87px;background:linear-gradient(160deg,#e2e2e2,#3c3f45)" role="img" aria-label="Business team meeting"></div>
<div class="photo" style="left:913px;top:975px;width:146px;height:87px;background:linear-gradient(160deg,#eef1f3,#a8b1b8)" role="img" aria-label="Bright open office interior"></div>

<!-- services -->
<div class="abs services"></div>
<h2 class="abs heading center-title" style="top:1258px">Our Services</h2>
<p class="abs services-desc">It is a long established fact that a reader will be distracted by the readable content of a page when looking at its layout. The point of using Lorem Ipsum is that it has a more-or-less normal distribution of letters.</p>
<div class="photo" style="left:161px;top:1383px;width:212px;height:212px;background:linear-gradient(160deg,#3c8fb0,#c9b89b)" role="img" aria-label="Interior design living space with teal wall and lounge"></div>
<div class="service-label" style="left:161px;top:1603px">Interior<br>Design</div>
<div class="photo" style="left:383px;top:1420px;width:212px;height:212px;background:linear-gradient(160deg,#9a8a76,#4f4a44)" role="img" aria-label="Fitout workers reviewing drawings"></div>
<div class="service-label" style="left:383px;top:1641px">Fitout</div>
<div class="photo" style="left:605px;top:1383px;width:212px;height:212px;background:linear-gradient(160deg,#a8835f,#c8d26a 55%,#6d5c4b)" role="img" aria-label="Construction workers laying bricks"></div>
<div class="service-label" style="left:605px;top:1603px">Construction</div>
<div class="photo" style="left:827px;top:1420px;width:212px;height:212px;background:linear-gradient(160deg,#5a544e,#d9caa8)" role="img" aria-label="Project management team planning around a table"></div>
<div class="service-label" style="left:827px;top:1641px">Project<br>Management</div>
<div class="btn" style="left:495px;top:1718px;width:210px;height:34px;font-weight:400">CONTACT US FOR A QUOTE</div>

<!-- expertise -->
<div class="photo" style="left:0;top:1924px;width:1200px;height:388px;background:linear-gradient(90deg,#4a3d31,#8a7158 50%,#c8c0b4)" role="img" aria-label="Warm living room interior with lamp, sofa and timber shelving"></div>
<div class="abs exp-box"></div>
<h2 class="abs heading exp-title">Expertise In Both<br>Design &amp;<br>Construction</h2>
<div class="abs exp-frame"></div>
<div class="photo" style="left:141px;top:2312px;width:447px;height:296px;background:linear-gradient(160deg,#d7c6a8,#b7c2cc 50%,#8a8f95)" role="img" aria-label="Engineer in safety vest viewing a building under construction"></div>
<div class="abs exp-copy">
  <p>It is a long established fact that a reader will be distracted by the readable content of a page when looking at its layout. The point of using Lorem Ipsum is that it has a more-or-less normal distribution of letters, as opposed to using 'Content here, content here', making it look like readable English.</p>
  <p>It is a long established fact that a reader will be distracted by the readable content of a page when looking at its layout.</p>
</div>
<div class="btn" style="left:630px;top:2534px;width:118px;height:34px;font-weight:400">CONTACT US</div>

<!-- portfolio -->
<h2 class="abs heading center-title" style="top:2702px">Our Portfolio</h2>
<div class="photo" style="left:141px;top:2768px;width:225px;height:202px;background:linear-gradient(160deg,#3f4750,#c98e4a)" role="img" aria-label="Office breakout area with colourful seating"></div>
<div class="photo" style="left:141px;top:2975px;width:225px;height:273px;background:linear-gradient(180deg,#e6e8ea,#b9bec2)" role="img" aria-label="Bright open-plan workstations"></div>
<div class="photo" style="left:371px;top:2768px;width:225px;height:272px;background:linear-gradient(90deg,#a6774b,#d6d3cf)" role="img" aria-label="Timber panelled office with glass partitions"></div>
<div class="photo" style="left:371px;top:3045px;width:225px;height:203px;background:linear-gradient(160deg,#2d2d2d,#c8c3b6)" role="img" aria-label="Dining and lounge interior with plants"></div>
<div class="photo" style="left:601px;top:2768px;width:225px;height:202px;background:linear-gradient(160deg,#2f5a66,#1d2c33)" role="img" aria-label="Lounge with teal sofas and feature artwork"></div>
<div class="abs portfolio-note" style="left:601px;top:2975px;width:225px;height:273px;background:#2a2a2a">Lorem ipsum dolor sit amet, consectetur adipiscing elit, sed do eiusmod tempor incididunt ut labore et dolore magna aliqua.</div>
<div class="photo" style="left:831px;top:2768px;width:228px;height:272px;background:linear-gradient(160deg,#f2f2f0,#c9cccd)" role="img" aria-label="White reception desk interior"></div>
<div class="photo" style="left:831px;top:3045px;width:228px;height:203px;background:linear-gradient(160deg,#e9c67a,#4b3a2c)" role="img" aria-label="Library style shelving interior"></div>
<div class="btn" style="left:511px;top:3277px;width:178px;height:33px;font-weight:400">VIEW MORE PROJECTS</div>

<!-- testimonials -->
<div class="abs testimonials"></div>
<h2 class="abs heading center-title" style="top:3476px">Testimonials</h2>
<div class="arrow" style="left:40px;top:3614px"><svg width="20" height="12" viewBox="0 0 20 12"><path d="M19 6H2M7 1L2 6l5 5" stroke="#222" stroke-width="1.6" fill="none"/></svg></div>
<div class="arrow next" style="left:1098px;top:3614px"><svg width="20" height="12" viewBox="0 0 20 12"><path d="M1 6h17M13 1l5 5-5 5" stroke="#0a8df0" stroke-width="1.6" fill="none"/></svg></div>
<div class="t-card" style="left:197px;top:3542px">
  <svg class="t-quote" width="38" height="28" viewBox="0 0 38 28"><path fill="#0a8df0" d="M0 18C0 8 5 2 14 0l1 4c-5 2-7 5-7 9h6v15H0zM21 18c0-10 5-16 14-18l1 4c-5 2-7 5-7 9h6v15H21z"/></svg>
  Lorem ipsum dolor sit amet, consectetuer adipiscing elit, sed diam nonummy nibh euismod tincidunt ut laoreet dolo re magna aliquam erat volutpat. Ut wisi enim ad minim ve niam, quis nostrud exerci tation
</div>
<div class="t-card" style="left:629px;top:3542px">
  <svg class="t-quote" width="38" height="28" viewBox="0 0 38 28"><path fill="#0a8df0" d="M0 18C0 8 5 2 14 0l1 4c-5 2-7 5-7 9h6v15H0zM21 18c0-10 5-16 14-18l1 4c-5 2-7 5-7 9h6v15H21z"/></svg>
  Lorem ipsum dolor sit amet, consectetuer adipiscing elit, sed diam nonummy nibh euismod tincidunt ut laoreet dolo re magna aliquam erat volutpat. Ut wisi enim ad minim ve niam, quis nostrud exerci tation
</div>
<div class="avatar" style="left:200px;top:3762px" role="img" aria-label="Client portrait"></div>
<div class="t-name" style="left:287px;top:3777px">Owen Hartley</div>
<div class="t-role" style="left:287px;top:3798px">Lorem ipsum dolor</div>
<div class="avatar" style="left:633px;top:3762px" role="img" aria-label="Client portrait"></div>
<div class="t-name" style="left:720px;top:3777px">Clara Whitfield</div>
<div class="t-role" style="left:720px;top:3798px">Lorem ipsum dolor</div>
<div class="btn" style="left:541px;top:3847px;width:118px;height:34px;font-weight:400">CONTACT US</div>

<!-- contact -->
<h2 class="abs heading center-title" style="top:4048px">Contact Us</h2>
<div class="field" style="left:280px;top:4143px;width:312px"><div class="ico"><svg width="16" height="16" viewBox="0 0 24 24"><circle cx="12" cy="7" r="5" fill="#0a8df0"/><path d="M2 24c0-6 4-9 10-9s10 3 10 9z" fill="#0a8df0"/></svg></div><span class="lbl">Full Name<i>*</i></span></div>
<div class="field" style="left:607px;top:4143px;width:311px"><div class="ico"><svg width="14" height="18" viewBox="0 0 24 32"><path d="M12 0a12 12 0 0 0-12 12c0 9 12 20 12 20s12-11 12-20A12 12 0 0 0 12 0zm0 17a5 5 0 1 1 0-10 5 5 0 0 1 0 10z" fill="#0a8df0"/></svg></div><span class="lbl">Company Address</span></div>
<div class="field" style="left:280px;top:4198px;width:312px"><div class="ico"><svg width="16" height="16" viewBox="0 0 24 24"><path d="M23 1L1 10l8 3 3 9 4-6 6 4z" fill="#0a8df0"/></svg></div><span class="lbl">Email Address</span></div>
<div class="field" style="left:607px;top:4198px;width:311px"><div class="ico"><svg width="16" height="16" viewBox="0 0 24 24"><path fill="#0a8df0" d="M6.6 10.8a15 15 0 0 0 6.6 6.6l2.2-2.2c.3-.3.7-.4 1-.2 1.1.4 2.3.6 3.6.6.6 0 1 .4 1 1V20c0 .6-.4 1-1 1A17 17 0 0 1 3 4c0-.6.4-1 1-1h3.5c.6 0 1 .4 1 1 0 1.3.2 2.5.6 3.6.1.3 0 .7-.2 1z"/></svg></div><span class="lbl">Phone Number<i>*</i></span></div>
<div class="field msg" style="left:280px;top:4253px;width:638px;height:80px"><div class="ico"><svg width="18" height="16" viewBox="0 0 24 22"><path d="M2 0h20a2 2 0 0 1 2 2v12a2 2 0 0 1-2 2H9l-6 6v-6H2a2 2 0 0 1-2-2V2a2 2 0 0 1 2-2z" fill="#0a8df0"/><path d="M5 5h14M5 9h10" stroke="#fff" stroke-width="1.6"/></svg></div><span class="lbl">Message<i>*</i></span></div>
<div class="btn" style="left:536px;top:4373px;width:127px;height:34px;font-weight:400">GET IN TOUCH</div>

<!-- footer -->
<div class="abs footer"></div>
<div class="brand" style="left:141px;top:4585px"><div class="brand-mark"></div><div class="brand-name">Harbor Shell Interiors</div></div>
<nav class="abs footer-nav"><span>HOME</span><span>SERVICES</span><span>PORTFOLIO</span><span>CONTACT US</span></nav>
<div class="f-info" style="left:498px;top:4598px"><div class="circ"><svg width="10" height="13" viewBox="0 0 24 32"><path d="M12 0a12 12 0 0 0-12 12c0 9 12 20 12 20s12-11 12-20A12 12 0 0 0 12 0zm0 17a5 5 0 1 1 0-10 5 5 0 0 1 0 10z" fill="#0a8df0"/></svg></div><div>Level 4, 52 Tidewater Street,<br>Melbourne VIC 3000</div></div>
<div class="f-info" style="left:732px;top:4598px"><div class="circ"><svg width="12" height="12" viewBox="0 0 24 24"><path fill="#0a8df0" d="M6.6 10.8a15 15 0 0 0 6.6 6.6l2.2-2.2c.3-.3.7-.4 1-.2 1.1.4 2.3.6 3.6.6.6 0 1 .4 1 1V20c0 .6-.4 1-1 1A17 17 0 0 1 3 4c0-.6.4-1 1-1h3.5c.6 0 1 .4 1 1 0 1.3.2 2.5.6 3.6.1.3 0 .7-.2 1z"/></svg></div><div><b>Phone</b><br>03 5550 1482</div></div>
<div class="f-info" style="left:887px;top:4598px"><div class="circ"><svg width="12" height="9" viewBox="0 0 24 18"><rect width="24" height="18" rx="2" fill="#0a8df0"/><path d="M1 2l11 8 11-8" stroke="#0b0b0b" stroke-width="2" fill="none"/></svg></div><div><b>Email</b><br>info@harborshell.com</div></div>
<div class="abs legal"></div>
<div class="abs legal-text">© 2024 Harbor Shell Interiors. All Rights Reserved.</div>
<div class="social" style="left:925px"></div>
<div class="social" style="left:960px"></div>
<div class="social" style="left:995px"></div>
<div class="social" style="left:1030px"></div>

</body>
</html>
```